TELVA EV

We need a business card design for a new Luxury golf cart Company Telva. We manufacture and sell high end golf carts. We would like to see designs that are high end. I have the logo so really need a nice clean look.

```html
<!DOCTYPE html>
<html lang="en">
<head>
<meta charset="utf-8">
<title>Telva EV – Business Card</title>
<link rel="stylesheet" href="https://fonts.googleapis.com/css2?family=Montserrat:wght@400;600;800&display=swap">
<style>
  :root {
    --bg: #2b2b2d;
    --card: #25262a;
    --teal: #0f7a63;
    --silver: #cfd1d3;
    --text: #e9eaeb;
  }
  * { margin: 0; padding: 0; box-sizing: border-box; }
  html, body { width: 1200px; height: 900px; overflow: hidden; }
  body {
    background: var(--bg);
    font-family: "Montserrat", sans-serif;
    display: flex;
    flex-direction: column;
    align-items: center;
    justify-content: center;
    gap: 44px;
  }
  .card {
    width: 660px;
    height: 377px;
    background: var(--card);
    border-radius: 22px;
    position: relative;
    box-shadow: 0 18px 40px rgba(0,0,0,.45);
  }
  .wordmark {
    font-weight: 800;
    color: var(--silver);
    letter-spacing: 6px;
    line-height: 1;
  }
  .card--front { display: flex; align-items: center; justify-content: center; }
  .card--front .wordmark { font-size: 92px; }

  .card--back .wordmark {
    position: absolute; top: 62px; left: 0; right: 0;
    text-align: center; font-size: 74px;
  }
  .details {
    position: absolute; top: 186px; left: 0; right: 0;
    display: flex; justify-content: center; align-items: stretch; gap: 22px;
  }
  .person { text-align: right; padding-top: 28px; }
  .person__name { color: var(--teal); font-weight: 600; font-size: 24px; }
  .person__role { color: var(--text); font-size: 13px; margin-top: 2px; }
  .divider { width: 1.5px; background: var(--teal); }
  .contact { list-style: none; color: var(--text); font-size: 14px; }
  .contact li { display: flex; align-items: center; gap: 10px; height: 22px; }
  .contact svg { width: 12px; height: 12px; fill: var(--teal); flex: none; }
  .address {
    position: absolute; bottom: 58px; left: 0; right: 0;
    text-align: center; color: var(--text); font-size: 15px;
  }
</style>
</head>
<body>
  <section class="card card--front">
    <div class="wordmark">TELVA</div>
  </section>

  <section class="card card--back">
    <div class="wordmark">TELVA</div>
    <div class="details">
      <div class="person">
        <div class="person__name">Arlen Voss</div>
        <div class="person__role">Owner</div>
      </div>
      <div class="divider"></div>
      <ul class="contact">
        <li><svg viewBox="0 0 24 24"><path d="M6.6 10.8a15 15 0 0 0 6.6 6.6l2.2-2.2a1 1 0 0 1 1-.25 11.4 11.4 0 0 0 3.6.57 1 1 0 0 1 1 1V20a1 1 0 0 1-1 1A17 17 0 0 1 3 4a1 1 0 0 1 1-1h3.5a1 1 0 0 1 1 1c0 1.25.2 2.45.57 3.57a1 1 0 0 1-.25 1z"/></svg>555-204-7718</li>
        <li><svg viewBox="0 0 24 24"><path d="M2 5h20v14H2zm2 2v.5l8 5 8-5V7z"/></svg>info@telva.com</li>
        <li><svg viewBox="0 0 24 24"><circle cx="12" cy="12" r="10"/></svg>www.telva.com</li>
      </ul>
    </div>
    <div class="address">48 Harbor Lane, Suite 210, Fairview, TX75000</div>
  </section>
</body>
</html>
```